Flyer für Reifen- und Autoservicebetrieb
Zielgruppe
Wir sind ein Reifen- und Autoservicebetrieb; eine freie KFZ-Meister-Werkstatt ohne Markenbindung.
Aufgabenstellung
Im Focus des Flyers soll auf der Vorderseite der Reifenservice stehen, da dieser zur bevorstehenden Winterreifen-Wechselsaison erscheinen wird (Reifenwechsel, Einlagerung, Räderwäsche, Online-Termin). Auf der Rückseite soll der Autoservice und der 'neu' angebotene LKW- und Landwirtschafts- Reifenservice beworben werden.

```html
<!DOCTYPE html>
<html lang="de">
<head>
<meta charset="utf-8">
<title>Korvel Reifen – Flyer</title>
<link rel="stylesheet" href="https://fonts.googleapis.com/css2?family=Exo+2:wght@300;400;500;600;700;800&display=swap">
<style>
  :root{
    --bg:#ffffff;
    --orange:#f4a31c;
    --ink:#2f2f2f;
    --pill:#333333;
    --body-grey:#d3d3d3;
    --light-grey:#e1e3e5;
    --white:#ffffff;
  }
  *{box-sizing:border-box;margin:0;padding:0}
  html,body{width:1200px;height:2560px;overflow:hidden;background:var(--bg)}
  body{position:relative;font-family:"Exo 2",sans-serif;color:var(--ink)}
  .page{position:absolute;left:217px;width:789px;background:var(--body-grey);box-shadow:0 14px 40px rgba(0,0,0,.28);overflow:hidden}
  .page--front{top:97px;height:1141px}
  .page--back{top:1333px;height:1128px}
  .shapes{position:absolute;left:0;top:0;width:789px}
  .brand{position:absolute;left:0;width:100%;display:flex;justify-content:center;align-items:center;gap:12px;font-weight:700;font-size:40px;color:var(--orange);letter-spacing:.5px}
  .brand__dot{width:22px;height:22px;border-radius:50%;background:#8a8a8a}
  .headline{position:absolute;left:0;top:512px;width:100%;text-align:center;font-weight:700;font-size:46px;line-height:55px;color:var(--ink)}
  .pill{position:absolute;background:var(--pill);color:var(--white);border-radius:26px;display:flex;align-items:center;justify-content:center;font-weight:600}
  .list{position:absolute;left:0;width:100%;text-align:center;font-weight:400;font-size:20px;color:var(--ink)}
  .list li{list-style:none}
  .label{position:absolute;left:0;width:100%;text-align:center;font-weight:700;font-size:19px}
  .spaced{position:absolute;left:0;width:100%;text-align:center;font-weight:400;font-size:19px;letter-spacing:6px}
  .badge-new{position:absolute;left:349px;top:689px;width:102px;height:36px;border-radius:18px;background:var(--orange);color:var(--white);font-weight:700;font-size:19px;display:flex;align-items:center;justify-content:center}
  .arc-title{position:absolute;left:0;top:845px;width:789px;height:80px}
</style>
</head>
<body>

<section class="page page--front">
  <svg class="shapes" height="1141" viewBox="0 0 789 1141">
    <defs>
      <linearGradient id="tyrePhoto" x1="0" y1="0" x2="0" y2="1">
        <stop offset="0" stop-color="#f4f4f4"/>
        <stop offset=".45" stop-color="#a9adb2"/>
        <stop offset="1" stop-color="#4a4d52"/>
      </linearGradient>
    </defs>
    <rect x="0" y="0" width="789" height="500" fill="url(#tyrePhoto)" role="img" aria-label="Foto: Mechaniker mit Handschuhen hält einen Winterreifen in der Werkstatt"/>
    <polygon points="0,468 395,492 789,468 789,625 395,653 0,625" fill="var(--orange)"/>
  </svg>
  <div class="brand" style="top:58px"><span class="brand__dot"></span>Korvel Reifen</div>
  <h1 class="headline">Ihr Experte für hochwertige<br>Reifen und Service</h1>
  <div class="pill" style="left:141px;top:676px;width:516px;height:50px;font-size:19px">Wartung und Pflege für Ihre Räder und Reifen</div>
  <ul class="list" style="top:735px;line-height:28.4px">
    <li>- Winterreifen</li>
    <li>- Rädereinlagerung</li>
    <li>- Reifenmontage</li>
    <li>- Auswuchten</li>
    <li>- Reifencheck</li>
    <li>- Reifenreparatur</li>
    <li>- Luftdruckkontrolle</li>
    <li>- Kalibrierung des Reifendruckkontrollsystems</li>
    <li>- Räderwäsche</li>
    <li>- Saisonaler Räder-/ Reifenwechsel</li>
  </ul>
  <div class="label" style="top:1050px">Online-Termin:</div>
  <div class="spaced" style="top:1076px">www.KORVEL-REIFEN.de</div>
</section>

<section class="page page--back">
  <svg class="shapes" height="1128" viewBox="0 0 789 1128">
    <defs>
      <linearGradient id="garagePhoto" x1="0" y1="0" x2="0" y2="1">
        <stop offset="0" stop-color="#eef0f3"/>
        <stop offset=".5" stop-color="#8ea3c4"/>
        <stop offset="1" stop-color="#3b4a6a"/>
      </linearGradient>
    </defs>
    <rect x="0" y="0" width="789" height="80" fill="#f7f7f7"/>
    <polygon points="0,70 789,70 789,402 395,429 0,402" fill="url(#garagePhoto)" role="img" aria-label="Foto: Werkstatthalle mit Hebebühne, Auto und blauen Werkzeugwagen"/>
    <polygon points="0,805 395,832 789,805 789,1128 0,1128" fill="var(--light-grey)"/>
  </svg>
  <div class="brand" style="top:58px"><span class="brand__dot"></span>Korvel Reifen</div>
  <div class="pill" style="left:254px;top:461px;width:292px;height:38px;font-size:22px">Unser Kfz-Service</div>
  <ul class="list" style="top:510px;line-height:28.5px">
    <li>- Inspektion - Ölservice - &nbsp;Klimaservice</li>
    <li>- Fehlerdiagnose - Stossdämpfer Service</li>
    <li>- Hauptuntersuchung/ Abgasuntersuchung (HU/AU)</li>
    <li>- Bremsenservice - Wintercheck - Batterieservice</li>
    <li>- Fahrzeugreparaturservice</li>
  </ul>
  <div class="badge-new">neu</div>
  <ul class="list" style="top:733px;line-height:28px">
    <li>- &nbsp;angebotene LKW</li>
    <li>- und Landwirtschafts Reifenservice</li>
  </ul>
  <svg class="arc-title" viewBox="0 0 789 80">
    <path id="arcPath" d="M250,75 Q395,30 545,75" fill="none"/>
    <text font-family="Exo 2, sans-serif" font-weight="700" font-size="26" fill="var(--ink)" text-anchor="middle">
      <textPath href="#arcPath" startOffset="50%">für PKW &amp; Transporter</textPath>
    </text>
  </svg>
  <div class="label" style="top:908px;font-size:20px">Öffnungszeiten</div>
  <div class="spaced" style="top:938px;line-height:23px">Montag - Freitag<br>8-12 Uhr und 12:30 - 17 Uhr</div>
  <div class="spaced" style="top:1019px;line-height:23px">Lindenweg 12, D-23999 Musterfeld<br>Tel.: 04000 123 45 67<br>info@korvel-reifen.de</div>
</section>

</body>
</html>
```